Business Card Design

We are a contracting firm, 95% of my work is interior renovations.... but also don't want to preclude the idea of doing exterior work if it arises. I Need a business card that says I am the ultimate professional. There is a per-determined notion that all contractors are shady, unreliable, etc. Being that most of my work is in Manhattan, I would like to give the impression of fresh, modern, sleek, design/build firm.

Target Market(s)

young couples 25-40

Industry/Entity Type

Business

Contact Information for Business Card

PeterHollowayBuilders LLC
27 North Birchwood Lane
Elm Hollow NY 11000
718-555-0193
646-555-0148- cell
www.phbrx.com
ph@phbrx.com
Peter Holloway

Requirements
Should not have
• do not want to give the impression of a "bargain basement store"

```html
<!DOCTYPE html>
<html lang="en">
<head>
<meta charset="utf-8">
<title>Peter Holloway Builders – Business Card</title>
<link href="https://fonts.googleapis.com/css2?family=Marcellus&family=Exo+2:wght@400;500&display=swap" rel="stylesheet">
<style>
  :root {
    --page: #e9e6e1;
    --card-white: #ffffff;
    --card-dark: #232325;
    --navy: #3a3a8c;
    --blue: #1f8fd6;
    --grey: #8a8a8a;
    --ink: #2b2b33;
    --icon: #4b3f9a;
  }
  * { margin: 0; padding: 0; box-sizing: border-box; }
  html, body { width: 1200px; height: 981px; overflow: hidden; background: var(--page); }
  .stage {
    width: 1200px; height: 981px;
    display: flex; flex-direction: column; align-items: center; justify-content: center; gap: 60px;
  }
  .card {
    position: relative; width: 700px; height: 400px;
    box-shadow: 0 4px 14px rgba(0,0,0,0.18);
  }
  .card--front { background: var(--card-white); }
  .card--back { background: var(--card-dark); display: flex; align-items: center; justify-content: center; }

  .wordmark { font-family: "Marcellus", serif; color: var(--navy); text-align: center; letter-spacing: 1px; }
  .wordmark__name { font-size: 30px; line-height: 1; }
  .wordmark__sub { font-size: 17px; letter-spacing: 9px; margin-top: 6px; }
  .card--front .wordmark { position: absolute; left: 48px; top: 150px; color: var(--navy); }
  .card--back .wordmark { color: var(--blue); }
  .card--back .wordmark__name { font-size: 38px; }
  .card--back .wordmark__sub { font-size: 21px; letter-spacing: 12px; }

  .accent-line { position: absolute; left: 0; top: 0; width: 700px; height: 400px; }

  .person { position: absolute; right: 42px; top: 40px; text-align: right; font-family: "Exo 2", sans-serif; }
  .person__name { font-size: 22px; font-weight: 500; letter-spacing: 3px; color: var(--navy); text-transform: uppercase; }
  .person__title { font-size: 12px; letter-spacing: 3px; color: var(--ink); margin-top: 4px; text-transform: uppercase; }

  .contacts { position: absolute; left: 48px; top: 252px; list-style: none; font-family: "Exo 2", sans-serif; font-size: 14px; color: var(--ink); }
  .contacts li { display: flex; align-items: center; gap: 9px; height: 23px; }
  .contacts svg { width: 15px; height: 15px; flex: none; }
</style>
</head>
<body>
<main class="stage">
  <section class="card card--front" aria-label="Card front">
    <svg class="accent-line" viewBox="0 0 700 400" aria-hidden="true">
      <defs>
        <linearGradient id="lineFade" x1="0" y1="1" x2="1" y2="0">
          <stop offset="0" stop-color="#3a3a8c" stop-opacity="0.2"/>
          <stop offset="0.5" stop-color="#1f8fd6"/>
          <stop offset="1" stop-color="#3a3a8c"/>
        </linearGradient>
      </defs>
      <polygon points="250,262 670,108 670,112" fill="url(#lineFade)"/>
    </svg>

    <div class="wordmark">
      <div class="wordmark__name">PETER HOLLOWAY</div>
      <div class="wordmark__sub">BUILDERS</div>
    </div>

    <div class="person">
      <div class="person__name">Peter Holloway</div>
      <div class="person__title">Owner / C.E.O</div>
    </div>

    <ul class="contacts">
      <li>
        <svg viewBox="0 0 16 16"><circle cx="8" cy="8" r="8" fill="var(--icon)"/><path d="M5.5 4.5l1.3 1.6-.7 1c.5 1 1.2 1.8 2.2 2.3l1-.7 1.6 1.3-.8 1.2C7.7 11 5 8.3 4.5 5.3z" fill="#fff"/></svg>
        718-555-0193
      </li>
      <li>
        <svg viewBox="0 0 16 16"><circle cx="8" cy="8" r="8" fill="var(--icon)"/><rect x="5.5" y="3.8" width="5" height="8.4" rx="1" fill="#fff"/><rect x="6.4" y="5" width="3.2" height="5.2" fill="var(--icon)"/></svg>
        646-555-0148
      </li>
      <li>
        <svg viewBox="0 0 16 16"><circle cx="8" cy="8" r="8" fill="var(--icon)"/><rect x="4" y="5.2" width="8" height="5.6" fill="#fff"/><path d="M4 5.2l4 3 4-3" fill="none" stroke="var(--icon)" stroke-width="0.9"/></svg>
        ph@phbrx.com
      </li>
      <li>
        <svg viewBox="0 0 16 16"><circle cx="8" cy="8" r="8" fill="var(--icon)"/><circle cx="8" cy="8" r="4" fill="none" stroke="#fff" stroke-width="0.9"/><path d="M4 8h8M8 4c-2 2.4-2 5.6 0 8M8 4c2 2.4 2 5.6 0 8" fill="none" stroke="#fff" stroke-width="0.8"/></svg>
        www.phbrx.com
      </li>
      <li>
        <svg viewBox="0 0 16 16"><circle cx="8" cy="8" r="8" fill="var(--icon)"/><path d="M8 12.5s-3-3.2-3-5.3a3 3 0 016 0c0 2.1-3 5.3-3 5.3z" fill="#fff"/><circle cx="8" cy="7.2" r="1.1" fill="var(--icon)"/></svg>
        27 North Birchwood Lane, Elm Hollow NY 11000
      </li>
    </ul>
  </section>

  <section class="card card--back" aria-label="Card back">
    <div class="wordmark">
      <div class="wordmark__name">PETER HOLLOWAY</div>
      <div class="wordmark__sub">BUILDERS</div>
    </div>
  </section>
</main>
</body>
</html>
```